Bellmont Crestwood Engraving Awards

I want an ecommerce site where customers can review our in stock items and or select from our vendor on-line catalog when placing an order. I also need a place where they can enter the inscription information for each award. Will accept Coinvale payments. Also need a section for perpetual awards where they sign up for the monthly awards, they select the Master Plaque they want and also select the monthly award they want. Has to be for single awards or multi awards from a single customer. Current web site is www.TopLaurelTrophy.com and I need to keep the same address. You can review it for what we do but it’s old and done by "me".
The main focus of our sales are perpetual awards so that should be front and center on the main page. I would like the customer to enter their information on an order form and select the Mater Plaque and which Monthly they would like. They can also do a monthly without a Master Plaque. Once the order is submitted, I would like to receive an email message with all the information in the text of the email.
I am in the process of getting newer pictures of these items and they should be available by the end of the week if not sooner.
I would like the links to the catalogs to also be on the home page.
An “Ask a Question” would also me a good idea where they inter contact information, enter their question and I receive an email with their questions and information for my reply to them.
Our key phrase is “The Power of Thank You!” We would like to see this on every page and where ever you think it would apply. We sell to many different companies and organizations all over the United States.

Target Market(s)

Auto Dealers, Real Estate Brokers, Sales Organizations

Coding

Coded - Design and coding required

Number of Pages Required

4 page

Colors
0355a3
ec1f27
fbed22
f78f20
a54499

Requirements
Must have
• Perpetual Plaque with Monthly Awards
• On-Line ordering process with select buttons for the Master Plaque and which monthly.
• Place to enter inscription for award
• Links to my suppliers catalog - like on my current site. A way to order from the catalog and pay with Coinvale.
Nice to have
• search engine that would allow search of vendors catalog
• A section for sports and academic awards

```html
<!DOCTYPE html>
<html lang="en">
<head>
<meta charset="utf-8">
<title>Crestwood Awards — The Power of Thank You!</title>
<link href="https://fonts.googleapis.com/css2?family=Raleway:wght@400;500;600;700&family=Open+Sans:wght@400;600;700&display=swap" rel="stylesheet">
<style>
:root{
  --pink:#e4226b;
  --pink-dark:#d81a5e;
  --red:#ec1f27;
  --blue:#0a6fc0;
  --purple:#7e2c9f;
  --green:#1fa84a;
  --yellow:#fbc80a;
  --orange:#f7a21b;
  --orange-text:#f39a1e;
  --ink:#222;
  --muted:#8a8a8a;
  --line:#d6d6d6;
  --grey-band:#efefef;
  --footer:#232323;
  --footer-deep:#161616;
}
*{box-sizing:border-box;margin:0;padding:0}
html,body{width:1200px;height:3564px;overflow:hidden}
body{font-family:"Open Sans",Arial,sans-serif;color:var(--ink);background:#fff;position:relative}
.abs{position:absolute}
input,textarea{font-family:"Open Sans",Arial,sans-serif;border:1px solid var(--line);background:#fff;color:var(--ink);font-size:13px;padding:0 14px;outline:none}
input::placeholder,textarea::placeholder{color:#8d8d8d}

/* top strip & header */
.top-strip{left:0;top:0;width:1200px;height:24px;background:var(--pink)}
.site-header{left:0;top:24px;width:1200px;height:106px;background:#fff}
.brand{left:95px;top:38px;display:flex;align-items:center;gap:10px}
.brand-dot{width:22px;height:22px;border-radius:50%;background:var(--red)}
.brand-name{font-family:"Raleway",sans-serif;font-weight:600;font-size:20px;color:#333}
.main-nav{left:460px;top:44px;display:flex;gap:28px;font-family:"Raleway",sans-serif;font-weight:600;font-size:13px;color:#333}
.main-nav a{color:inherit;text-decoration:none;padding-bottom:8px}
.main-nav a.active{color:var(--orange-text);border-bottom:2px solid var(--orange-text)}
.icon-btn{top:40px;width:32px;height:32px;border-radius:50%;display:flex;align-items:center;justify-content:center}
.icon-cart{left:1030px;background:var(--pink)}
.icon-search{left:1070px;background:var(--orange)}

/* hero */
.hero{left:0;top:130px;width:1200px;height:516px;background:#0b0b0b;overflow:hidden}
.hero-visual{left:0;top:0;width:1200px;height:516px;background:radial-gradient(ellipse 480px 380px at 330px 220px,#fff3c6 0%,#e0b24a 22%,#8a5d16 48%,#2b1c08 72%,#050505 100%)}
.hero-copy{left:589px;top:292px;color:#fff}
.hero-title{font-family:"Raleway",sans-serif;font-weight:500;font-size:46px;line-height:1.1}
.hero-sub{font-family:"Raleway",sans-serif;font-weight:500;font-size:24px;margin-top:12px}
.hero-text{font-size:16px;line-height:1.5;margin-top:14px}
.hero-arrow{top:360px}

/* categories */
.categories{left:97px;top:668px;width:1003px;height:235px;display:flex}
.cat{flex:1;position:relative;text-align:center;color:#fff;border-bottom:8px solid rgba(0,0,0,.22)}
.cat-red{background:var(--red)}.cat-blue{background:var(--blue)}.cat-purple{background:var(--purple)}.cat-green{background:var(--green)}.cat-yellow{background:var(--yellow)}
.cat-thumb{width:120px;height:100px;margin:20px auto 0;border-radius:4px;background:linear-gradient(160deg,rgba(255,255,255,.55),rgba(0,0,0,.25))}
.cat-label{font-family:"Raleway",sans-serif;font-weight:500;font-size:19px;margin-top:14px}
.cat-btn{display:inline-block;margin-top:10px;border:2px solid #fff;padding:4px 22px;font-size:12px;font-weight:600;color:#fff}

/* forms row */
.panel{top:936px;height:625px;border:2px solid #dedede;background:#fff}
.panel-monthly{left:97px;width:495px}
.panel-catalog{left:613px;width:492px}
.panel-title{font-family:"Raleway",sans-serif;font-weight:500;font-size:27px;text-align:center;margin-top:30px;color:#1c1c1c}
.panel-desc{font-size:13px;color:var(--muted);text-align:center;line-height:1.5;width:400px;margin:10px auto 0}
.panel-kicker{font-family:"Raleway",sans-serif;font-size:19px;color:var(--orange-text);text-align:center;margin-top:6px}
.field{position:absolute;height:38px}
.textarea{position:absolute;height:72px;padding:10px 14px;resize:none}
.gender{position:absolute;display:flex;align-items:center;gap:12px;font-size:18px;font-family:"Raleway",sans-serif}
.gender label{display:flex;align-items:center;gap:6px;font-size:13px;color:#777;font-family:"Open Sans",sans-serif}
.radio{width:16px;height:16px;border:1px solid #bbb;border-radius:50%;display:inline-block}
.btn-red{position:absolute;background:var(--red);color:#fff;font-weight:700;font-size:14px;display:flex;align-items:center;justify-content:center}
.pay-row{position:absolute;display:flex;align-items:center;gap:5px;font-size:12px;color:#555;white-space:nowrap}
.pay-row .pay-mail{margin-right:8px}
.card-badge{height:18px;padding:0 4px;border-radius:2px;background:#e9eef5;border:1px solid #c9d2de;font-size:7px;font-weight:700;color:#33475f;display:flex;align-items:center}
.btn-pink{position:absolute;background:var(--pink);color:#fff;font-family:"Raleway",sans-serif;font-weight:600;font-size:20px;display:flex;align-items:center;justify-content:center;letter-spacing:.5px}

/* master plaques */
.plaque{top:1597px;width:316px;height:340px;border:2px solid #dedede;text-align:center;overflow:hidden}
.plaque-img{width:160px;height:158px;margin:24px auto 0;background:linear-gradient(160deg,#8b6a45,#3a2a1c)}
.plaque-name{font-family:"Raleway",sans-serif;font-weight:500;font-size:19px;line-height:1.4;margin-top:30px;color:#222}
.plaque-price{position:absolute;left:0;bottom:0;width:100%;height:58px;background:var(--orange);color:#fff;font-family:"Raleway",sans-serif;font-size:19px;display:flex;align-items:center;justify-content:center;border-radius:50% 50% 0 0/14px 14px 0 0}

/* grey order sections */
.order-band{left:0;width:1200px;background:var(--grey-band)}
.order-band::before{content:"";position:absolute;left:576px;top:0;border-left:22px solid transparent;border-right:22px solid transparent;border-top:20px solid #fff}
.section-title{position:absolute;left:0;width:1200px;text-align:center;font-family:"Raleway",sans-serif;font-weight:500;font-size:25px;letter-spacing:.5px;color:#1c1c1c}
.logo-choice{position:absolute;display:flex;align-items:center;gap:10px;font-size:17px;font-family:"Raleway",sans-serif;color:#333}
.logo-choice label{display:flex;align-items:center;gap:6px}
.box{width:18px;height:18px;background:#fff;border:1px solid #ccc;display:inline-block}
.artwork-note{position:absolute;font-size:13px;color:#444;white-space:nowrap}
.btn-yellow{position:absolute;background:var(--yellow);color:#fff;font-weight:600;font-size:19px;display:flex;align-items:center;justify-content:center;box-shadow:0 3px 0 #e0a800}

/* individual awards */
.awards-grid{left:95px;top:2426px;width:1000px;height:271px;display:flex;border:2px solid #dedede}
.award{flex:1;text-align:center;border-right:2px solid #dedede}
.award:last-child{border-right:0}
.award-img{width:80px;height:107px;margin:33px auto 0;background:linear-gradient(160deg,#9a9a9a,#222)}
.award-tag{font-weight:700;font-size:13px;color:var(--pink);margin-top:24px}
.award-price{font-weight:700;font-size:17px;margin-top:6px}
.award-select{display:inline-block;margin-top:8px;width:120px;height:29px;line-height:29px;background:var(--pink);color:#fff;font-weight:700;font-size:13px}

/* shipping / newsletter */
.ship{left:0;top:3086px;width:601px;height:131px;background:var(--pink);color:#fff}
.ship-text{position:absolute;left:245px;top:36px;font-family:"Raleway",sans-serif;font-size:23px;line-height:1.3}
.ship-text b{font-weight:700;font-size:28px}
.newsletter{left:601px;top:3086px;width:599px;height:131px;background:var(--pink-dark);color:#fff}
.news-title{position:absolute;left:25px;top:26px;font-family:"Raleway",sans-serif;font-size:21px}
.news-title b{font-weight:700}
.news-input{position:absolute;left:25px;top:67px;width:292px;height:38px;border:0}
.news-btn{position:absolute;left:328px;top:67px;width:135px;height:38px;background:var(--orange);font-weight:700;font-size:13px;display:flex;align-items:center;justify-content:center}

/* footer */
.footer{left:0;top:3217px;width:1200px;height:288px;background:var(--footer);color:#ddd}
.foot-col{position:absolute;top:48px}
.foot-col h4{font-family:"Raleway",sans-serif;font-weight:700;font-size:14px;color:#fff;letter-spacing:.5px;padding-bottom:12px;border-bottom:1px solid #555;width:165px}
.foot-col ul{list-style:none;margin-top:22px}
.foot-col li{font-size:13px;line-height:29px;color:#cfcfcf}
.foot-col li::before{content:"»";margin-right:30px;color:#fff}
.bottom-bar{left:0;top:3505px;width:1200px;height:59px;background:var(--footer-deep)}
.copyright{position:absolute;left:100px;top:21px;font-size:12px;color:#999}
.bottom-pay{position:absolute;left:826px;top:20px;display:flex;gap:8px}
</style>
</head>
<body>

<div class="abs top-strip"></div>

<header class="abs site-header">
  <div class="abs brand"><span class="brand-dot"></span><span class="brand-name">Crestwood Awards</span></div>
  <nav class="abs main-nav">
    <a class="active" href="#">HOME</a>
    <a href="#">PERPETUAL PROGRAM</a>
    <a href="#">CATALOG ORDER FORM</a>
    <a href="#">MONTHLY SUBMISSION</a>
  </nav>
  <div class="abs icon-btn icon-cart">
    <svg width="16" height="16" viewBox="0 0 16 16"><path d="M1 2h2.5l2 8h7l1.8-6H5" fill="none" stroke="#fff" stroke-width="1.8"/><circle cx="6.5" cy="13.5" r="1.3" fill="#fff"/><circle cx="11.5" cy="13.5" r="1.3" fill="#fff"/></svg>
  </div>
  <div class="abs icon-btn icon-search">
    <svg width="16" height="16" viewBox="0 0 16 16"><circle cx="6.5" cy="6.5" r="4.3" fill="none" stroke="#fff" stroke-width="2"/><path d="M10 10l4.5 4.5" stroke="#fff" stroke-width="2.2"/></svg>
  </div>
</header>

<section class="abs hero">
  <div class="abs hero-visual" role="img" aria-label="Golden trophy cup with glowing light rays on a dark background"></div>
  <svg class="abs hero-arrow" style="left:55px" width="32" height="56" viewBox="0 0 32 56"><path d="M28 2L4 28l24 26" fill="none" stroke="rgba(255,255,255,.45)" stroke-width="2"/></svg>
  <svg class="abs hero-arrow" style="left:1110px" width="32" height="56" viewBox="0 0 32 56"><path d="M4 2l24 26L4 54" fill="none" stroke="rgba(255,255,255,.45)" stroke-width="2"/></svg>
  <div class="abs hero-copy">
    <h1 class="hero-title">The Power of Thank You!</h1>
    <p class="hero-sub">Perpetual, Monthly and Individual Awards</p>
    <p class="hero-text">Motivate your team memebrs, sales force, service organization,<br>to exceed expectations and be the top performers.</p>
  </div>
</section>

<section class="abs categories">
  <div class="cat cat-red"><div class="cat-thumb" role="img" aria-label="Acrylic award pieces"></div><div class="cat-label">Premier Acrylic</div><span class="cat-btn">Click here</span></div>
  <div class="cat cat-blue"><div class="cat-thumb" role="img" aria-label="Crystal award"></div><div class="cat-label">Premier Crystal</div><span class="cat-btn">Click here</span></div>
  <div class="cat cat-purple"><div class="cat-thumb" role="img" aria-label="Perpetual plaques"></div><div class="cat-label">Perpetual Program</div><span class="cat-btn">Click here</span></div>
  <div class="cat cat-green"><div class="cat-thumb" role="img" aria-label="Wooden corporate award"></div><div class="cat-label">Corporate Awards</div><span class="cat-btn">Click here</span></div>
  <div class="cat cat-yellow"><div class="cat-thumb" role="img" aria-label="Sports trophies"></div><div class="cat-label">Sports &amp; Academic</div><span class="cat-btn">Click here</span></div>
</section>

<section class="abs panel panel-monthly">
  <h2 class="panel-title">MONTHLY SUBMISSION</h2>
  <p class="panel-desc">Maecenas aliquet velit vel turpis Mauris neque metus malesuada nec ultricies sit amet porttitor mattis enim</p>
  <input class="field" style="left:65px;top:150px;width:401px" placeholder="Company Name:">
  <input class="field" style="left:65px;top:200px;width:401px" placeholder="Winner's Name:">
  <input class="field" style="left:65px;top:250px;width:401px" placeholder="Your Email Address:">
  <input class="field" style="left:65px;top:300px;width:401px" placeholder="Month of the Award">
  <input class="field" style="left:65px;top:350px;width:401px" placeholder="Winner's Title: Salesperson/Employee/Tech">
  <input class="field" style="left:65px;top:400px;width:160px" placeholder="Today's Date:">
  <div class="gender" style="left:240px;top:407px">Gender <label><span class="radio"></span>Male</label><label><span class="radio"></span>Female</label></div>
  <textarea class="textarea" style="left:65px;top:452px;width:392px" placeholder="Service Instruction:"></textarea>
  <div class="btn-red" style="left:65px;top:542px;width:125px;height:36px">SUBMIT</div>
</section>

<section class="abs panel panel-catalog">
  <h2 class="panel-title">ABOUT US</h2>
  <p class="panel-kicker">Order from Catalog Form</p>
  <input class="field" style="left:53px;top:115px;width:396px;height:36px" placeholder="Full Name">
  <input class="field" style="left:53px;top:164px;width:196px;height:36px" placeholder="Email address">
  <input class="field" style="left:253px;top:164px;width:196px;height:36px" placeholder="Price of Award">
  <input class="field" style="left:53px;top:213px;width:396px;height:36px" placeholder="Company Name">
  <input class="field" style="left:53px;top:262px;width:196px;height:36px" placeholder="Quantity of Awards">
  <input class="field" style="left:253px;top:262px;width:196px;height:36px" placeholder="Order type">
  <input class="field" style="left:53px;top:311px;width:196px;height:36px" placeholder="Contact Name">
  <input class="field" style="left:253px;top:311px;width:196px;height:36px" placeholder="Title">
  <input class="field" style="left:53px;top:360px;width:396px;height:36px" placeholder="Program Type">
  <input class="field" style="left:53px;top:409px;width:396px;height:36px" placeholder="Billing Address:">
  <input class="field" style="left:53px;top:458px;width:196px;height:36px" placeholder="Date">
  <input class="field" style="left:253px;top:458px;width:196px;height:36px" placeholder="Code">
  <div class="pay-row" style="left:53px;top:505px"><span class="pay-mail">Sales@CrestwoodAwardsShop.com</span>
    <span class="card-badge">Veritas</span><span class="card-badge">Amerix</span><span class="card-badge">Discova</span><span class="card-badge">Meridian</span><span class="card-badge">Coinvale</span>
  </div>
  <div class="btn-pink" style="left:57px;top:545px;width:396px;height:52px">SUBMIT NOW</div>
</section>

<div class="abs plaque" style="left:105px"><div class="plaque-img" role="img" aria-label="Master plaque with monthly award, traditional style"></div><p class="plaque-name">Master Plaque &amp;<br>Monthly Award Traditional</p><div class="plaque-price">Just $45/Month</div></div>
<div class="abs plaque" style="left:447px"><div class="plaque-img" style="background:linear-gradient(160deg,#3a3a3a,#0c0c0c)" role="img" aria-label="Master plaque with monthly award, contemporary black style"></div><p class="plaque-name">Master Plaque &amp;<br>Monthly Award Contemporary</p><div class="plaque-price">Just $31/Month</div></div>
<div class="abs plaque" style="left:789px"><div class="plaque-img" style="background:linear-gradient(160deg,#6e4a33,#2a1a12)" role="img" aria-label="Master plaque with monthly award in walnut with glass award"></div><p class="plaque-name">Master Plaque &amp;<br>Monthly Award Walnut Grove</p><div class="plaque-price">Just $46/Month</div></div>

<section class="abs order-band" style="top:1977px;height:347px">
  <h2 class="section-title" style="top:45px">ORDER THE SET AND SAVE</h2>
  <input class="field" style="left:166px;top:97px;width:274px" placeholder="Customer Name">
  <input class="field" style="left:454px;top:97px;width:275px" placeholder="Attention">
  <input class="field" style="left:744px;top:97px;width:278px" placeholder="Address">
  <input class="field" style="left:166px;top:150px;width:274px" placeholder="Contact">
  <input class="field" style="left:454px;top:150px;width:275px" placeholder="Phone">
  <input class="field" style="left:744px;top:150px;width:278px" placeholder="Data of Order">
  <input class="field" style="left:166px;top:202px;width:274px" placeholder="Program Type">
  <div class="logo-choice" style="left:461px;top:211px">Logo ? <label><span class="box"></span>Yes</label><label><span class="box"></span>No</label></div>
  <p class="artwork-note" style="left:672px;top:213px">(Artwork files can be emaile d to sales@crestwoodawardsshop.com )</p>
  <div class="btn-yellow" style="left:504px;top:268px;width:176px;height:42px">SUBMIT</div>
</section>

<h2 class="section-title abs" style="top:2367px">INDIVIDUAL AWARDS</h2>
<section class="abs awards-grid">
  <div class="award"><div class="award-img" style="background:linear-gradient(160deg,#444,#0d0d0d)" role="img" aria-label="Black plaque award"></div><p class="award-tag">MONTHLY AWARDS</p><p class="award-price">$89.00</p><span class="award-select">SELECT</span></div>
  <div class="award"><div class="award-img" style="background:linear-gradient(160deg,#a32a25,#4a0e0c)" role="img" aria-label="Red plaque award"></div><p class="award-tag">MONTHLY AWARDS</p><p class="award-price">$87.00</p><span class="award-select">SELECT</span></div>
  <div class="award"><div class="award-img" style="background:linear-gradient(160deg,#e4e7ea,#8c949c);width:50px" role="img" aria-label="Glass tower award"></div><p class="award-tag">MONTHLY AWARDS</p><p class="award-price">$85.00</p><span class="award-select">SELECT</span></div>
  <div class="award"><div class="award-img" style="background:linear-gradient(160deg,#cfd3d6,#4b5056);width:56px" role="img" aria-label="Glass award on dark base"></div><p class="award-tag">MONTHLY AWARDS</p><p class="award-price">$79.00</p><span class="award-select">SELECT</span></div>
  <div class="award"><div class="award-img" style="background:linear-gradient(160deg,#f4f6f7,#a9b1b8);width:90px" role="img" aria-label="Crystal flame award"></div><p class="award-tag">MONTHLY AWARDS</p><p class="award-price">$79.00</p><span class="award-select">SELECT</span></div>
</section>

<section class="abs order-band" style="top:2744px;height:342px">
  <h2 class="section-title" style="top:48px">ORDER FORM</h2>
  <input class="field" style="left:166px;top:99px;width:277px" placeholder="Customer Name">
  <input class="field" style="left:456px;top:99px;width:278px" placeholder="Attention">
  <input class="field" style="left:748px;top:99px;width:277px" placeholder="Address">
  <input class="field" style="left:166px;top:154px;width:277px" placeholder="Contact">
  <input class="field" style="left:456px;top:154px;width:278px" placeholder="Phone">
  <input class="field" style="left:748px;top:154px;width:277px" placeholder="Data of Order">
  <input class="field" style="left:166px;top:206px;width:277px" placeholder="Program Type">
  <div class="logo-choice" style="left:461px;top:215px">Logo ? <label><span class="box"></span>Yes</label><label><span class="box"></span>No</label></div>
  <p class="artwork-note" style="left:674px;top:217px">(Artwork files can be emaile d to sales@crestwoodawardsshop.com )</p>
  <div class="btn-yellow" style="left:506px;top:271px;width:176px;height:42px">SUBMIT</div>
</section>

<section class="abs ship">
  <svg class="abs" style="left:160px;top:44px" width="66" height="46" viewBox="0 0 66 46"><rect x="0" y="4" width="40" height="28" fill="#fff"/><path d="M42 12h13l9 11v9H42z" fill="#fff"/><circle cx="13" cy="37" r="7" fill="#fff" stroke="#e4226b" stroke-width="3"/><circle cx="52" cy="37" r="7" fill="#fff" stroke="#e4226b" stroke-width="3"/></svg>
  <p class="ship-text"><b>FREE SHIPPING FOR</b><br>ORDERS OVER $100</p>
</section>
<section class="abs newsletter">
  <p class="news-title"><b>KEEP UPDATED.</b> SUBSCRIBE TO OUR NEWSLETTER!</p>
  <input class="news-input" placeholder="Enter Email Address">
  <div class="news-btn">SUBSCRIBE</div>
</section>

<footer class="abs footer">
  <div class="foot-col" style="left:105px"><h4>INFORMATION</h4><ul><li>Home</li><li>About us</li><li>Products</li><li>Blog</li><li>Contact us</li></ul></div>
  <div class="foot-col" style="left:368px"><h4>SHOPPING GUIDE</h4><ul><li>FAQs</li><li>Payment</li><li>Shipment</li><li>Where is my order?</li><li>Return policy</li></ul></div>
  <div class="foot-col" style="left:656px"><h4>MY ACCOUNT</h4><ul><li>My orders</li><li>My merchandise returns</li><li>My credit slips</li><li>My addresses</li><li>My personal info</li></ul></div>
  <div class="foot-col" style="left:943px"><h4>SOCIAL MEDIA LINKS</h4><ul><li>Friendbook</li><li>Chirpline</li><li>Proflink</li><li>Circleplus</li><li>Streamtube</li></ul></div>
</footer>
<div class="abs bottom-bar">
  <p class="copyright">Copyright © 2016 Crestwood Awards All rights reserved.</p>
  <div class="bottom-pay"><span class="card-badge">Veritas</span><span class="card-badge">Amerix</span><span class="card-badge">Discova</span><span class="card-badge">Meridian</span><span class="card-badge">Coinvale</span></div>
</div>

</body>
</html>
```